Commercial Business Card - stand out, clean, simple, unique.

commercial real estate group located in Texas. Called 4 Ridges Real Estate. We want a unique yet clean and professional card. On one side I would like the 4R to be by itself or to look as unique or tasteful as possible. We have the logo in white, black, and color in case a black background or something similar looks best on one side. We need a space for our name, email, cell. website. And possibly room for a phrase or city.

Contact Information for Business Card

Name, Title, Email, Phone Number, website

```html
<!DOCTYPE html>
<html lang="en">
<head>
<meta charset="utf-8">
<title>4 Ridges Real Estate – Business Card</title>
<link rel="stylesheet" href="https://fonts.googleapis.com/css2?family=Cinzel:wght@500&family=Lato:wght@400&display=swap">
<style>
  :root {
    --page-bg: #e4e4e6;
    --navy-light: #22459a;
    --navy: #1a3580;
    --navy-deep: #0e1e4e;
    --white: #ffffff;
    --shadow: rgba(20, 30, 60, 0.22);
  }
  html, body {
    margin: 0;
    padding: 0;
    width: 1200px;
    height: 900px;
    overflow: hidden;
    background: var(--page-bg);
  }
  .stage {
    position: relative;
    width: 1200px;
    height: 900px;
  }
  .card {
    position: absolute;
    top: 290px;
    width: 520px;
    height: 300px;
    border-radius: 22px;
    overflow: hidden;
    box-shadow: 0 6px 18px var(--shadow);
  }

  /* Back side */
  .card-back {
    left: 60px;
    background: linear-gradient(160deg, var(--navy-light) 0%, var(--navy) 45%, var(--navy-deep) 100%);
    display: flex;
    align-items: center;
    justify-content: center;
  }
  .back-name {
    font-family: "Cinzel", serif;
    font-weight: 500;
    font-size: 30px;
    letter-spacing: 2px;
    color: var(--white);
    text-transform: uppercase;
  }

  /* Front side */
  .card-front {
    left: 620px;
    background: var(--white);
  }
  .front-band {
    position: absolute;
    left: 120px;
    right: 0;
    top: 122px;
    bottom: 0;
    background: linear-gradient(160deg, var(--navy-light) 0%, var(--navy) 50%, var(--navy-deep) 100%);
  }
  .front-brand {
    position: absolute;
    right: 26px;
    top: 36px;
    text-align: right;
    font-family: "Cinzel", serif;
    font-weight: 500;
    font-size: 27px;
    line-height: 1.15;
    letter-spacing: 1px;
    color: var(--navy);
    text-transform: uppercase;
  }
  .corner-name {
    position: absolute;
    left: 0;
    width: 120px;
    bottom: 34px;
    text-align: center;
    font-family: "Cinzel", serif;
    font-weight: 500;
    font-size: 14px;
    line-height: 1.4;
    letter-spacing: 1px;
    color: var(--navy);
    text-transform: uppercase;
  }
  .contact {
    position: absolute;
    right: 26px;
    top: 136px;
    text-align: right;
    color: var(--white);
    font-family: "Lato", sans-serif;
    font-size: 14px;
  }
  .contact-name {
    font-family: "Cinzel", serif;
    font-weight: 500;
    font-size: 20px;
    letter-spacing: 1px;
    text-transform: uppercase;
    margin: 0;
  }
  .contact-title {
    margin: 0 0 12px;
    font-size: 14px;
  }
  .contact-line {
    display: flex;
    justify-content: flex-end;
    align-items: center;
    gap: 6px;
    margin: 0 0 6px;
  }
  .contact-line svg {
    width: 12px;
    height: 12px;
    fill: var(--white);
  }
</style>
</head>
<body>
<main class="stage">

  <section class="card card-back" aria-label="Business card back">
    <span class="back-name">4 Ridges Real Estate</span>
  </section>

  <section class="card card-front" aria-label="Business card front">
    <div class="front-band"></div>
    <div class="front-brand">4 Ridges<br>Real Estate</div>
    <div class="corner-name">4 Ridges<br>Real Estate</div>

    <div class="contact">
      <p class="contact-name">Daniel Harper</p>
      <p class="contact-title">Managing Director</p>
      <p class="contact-line">0412 555 730
        <svg viewBox="0 0 24 24" aria-hidden="true"><path d="M6.6 10.8a15.1 15.1 0 0 0 6.6 6.6l2.2-2.2a1 1 0 0 1 1-.25 11.4 11.4 0 0 0 3.6.57 1 1 0 0 1 1 1V20a1 1 0 0 1-1 1A17 17 0 0 1 3 4a1 1 0 0 1 1-1h3.5a1 1 0 0 1 1 1c0 1.25.2 2.45.57 3.6a1 1 0 0 1-.25 1z"/></svg>
      </p>
      <p class="contact-line">hello@ridgesmail.com
        <svg viewBox="0 0 24 24" aria-hidden="true"><path d="M2 5h20v14H2z M2 5l10 8 10-8" fill="none" stroke="#fff" stroke-width="2"/></svg>
      </p>
      <p class="contact-line">www.ridgeline-homes.com
        <svg viewBox="0 0 24 24" aria-hidden="true"><circle cx="12" cy="12" r="10" fill="none" stroke="#fff" stroke-width="2"/><path d="M2 12h20M12 2c3 3 3 17 0 20M12 2c-3 3-3 17 0 20" fill="none" stroke="#fff" stroke-width="1.6"/></svg>
      </p>
    </div>
  </section>

</main>
</body>
</html>
```